Business Cards for cafe providing speciality coffee and food

I need a business card design for my husband’s businesses. He has two cafes in Brisbane. The business name is Copperleaf Roasting House. They sell high end specialty coffee as well as breakfast and lunch. All the food is cooked fresh, in house and they have strict quality controls for their coffee. I would like the business card to feature the address for both cafes, my husband’s phone number and the business’s instagram. The address for the first is 61 Walden Crescent, Oakvale and the second is 23 Pellow Avenue, Brindlemoor. The Instagram handle is @copperleafroastinghouse and phone number is 0491362847. We already have a business logo that is attached.

Target Market(s)

All ages, higher disposable income and more likely to eat out regularly

Industry/Entity Type

Hospitality

Contact Information for Business Card

Must be suitable for both customers and suppliers

Font styles to use
Sans Serif

Colors

Designer to choose colors to be used in the design.

Requirements
Must have
• Owner’s name: Reid Castell
• Addresses of both cafes: 61 Walden Crescent, Oakvale and 23 Pellow Avenue, Brindlemoor
• Instagram handle: @copperleafroastinghouse
• Contact number: 0491362847
Nice to have
• Business logo

```html
<!DOCTYPE html>
<html lang="en">
<head>
<meta charset="utf-8">
<title>Copperleaf Roasting House – Business Cards</title>
<link rel="stylesheet" href="https://fonts.googleapis.com/css2?family=Oswald:wght@300;400;500&display=swap">
<style>
  :root {
    --page: #ffffff;
    --kraft-light: #dcc6a0;
    --kraft-dark: #c4a577;
    --ink-dark: #111111;
    --slate-light: #4a4a4a;
    --slate-dark: #2c2c2c;
    --ink-light: #ffffff;
  }
  * { margin: 0; padding: 0; box-sizing: border-box; }
  html, body { width: 1033px; height: 1200px; overflow: hidden; background: var(--page); }
  body { position: relative; font-family: "Oswald", sans-serif; }

  .card { position: absolute; left: 14px; width: 1005px; overflow: hidden; }
  .card--kraft { top: 14px; height: 576px; color: var(--ink-dark); --ink: var(--ink-dark);
    background: radial-gradient(ellipse at 60% 20%, var(--kraft-light), var(--kraft-dark)); }
  .card--slate { top: 612px; height: 574px; color: var(--ink-light); --ink: var(--ink-light);
    background: radial-gradient(ellipse at 50% 40%, var(--slate-light), var(--slate-dark)); }

  .card__frame { position: absolute; inset: 0; width: 100%; height: 100%; }
  .card__frame line { stroke: var(--ink); stroke-width: 4; }

  .card__backdrop { position: absolute; left: 345px; top: 225px; width: 630px; height: 345px;
    background: radial-gradient(ellipse at 70% 70%, rgba(255,255,255,0.18), rgba(255,255,255,0) 65%); }

  .brand { position: absolute; width: 350px; height: 350px; border-radius: 50%;
    border: 6px solid var(--ink); display: flex; align-items: center; justify-content: center;
    text-align: center; font-weight: 500; font-size: 40px; line-height: 1.15; letter-spacing: 3px;
    text-transform: uppercase; padding: 40px; }
  .card--kraft .brand { left: 64px; top: 90px; }
  .card--slate .brand { left: 67px; top: 98px; }

  .icon-box { position: absolute; }
  .icon-box--persona { left: 445px; width: 92px; height: 50px; border-radius: 25px;
    background: var(--ink); opacity: 0.85; }
  .card--kraft .icon-box--persona { top: 186px; }
  .card--slate .icon-box--persona { top: 184px; }
  .icon-box--beans { left: 565px; top: 22px; width: 100px; height: 78px; border-radius: 40px;
    background: var(--ink); }

  .phone-icon { position: absolute; left: 455px; width: 72px; height: 72px; }
  .card--kraft .phone-icon { top: 289px; }
  .card--slate .phone-icon { top: 287px; }

  .owner, .phone { position: absolute; left: 566px; font-weight: 300; text-transform: uppercase; white-space: nowrap; }
  .owner { font-size: 56px; letter-spacing: 8px; line-height: 1; top: 180px; }
  .phone { font-size: 62px; letter-spacing: 5px; line-height: 1; }
  .card--kraft .phone { top: 290px; }
  .card--slate .phone { top: 288px; }

  .contact-row { position: absolute; left: 18px; right: 24px; display: flex; align-items: center;
    font-weight: 500; font-size: 26px; letter-spacing: 2.5px; text-transform: uppercase; white-space: nowrap; }
  .card--kraft .contact-row { top: 508px; }
  .card--slate .contact-row { top: 512px; }
  .pin-icon { width: 28px; height: 40px; margin-right: 14px; flex: none; }
  .social-mark { width: 38px; height: 38px; border: 4px solid var(--ink); border-radius: 9px;
    margin-left: auto; margin-right: 12px; flex: none; }
</style>
</head>
<body>

<section class="card card--kraft">
  <div class="card__backdrop" role="img" aria-label="Faint line illustration of a cafe skyline with a coffee cup"></div>
  <svg class="card__frame" viewBox="0 0 1005 576" aria-hidden="true">
    <line x1="18" y1="54" x2="203" y2="54"/><line x1="20" y1="52" x2="20" y2="233"/>
    <line x1="795" y1="54" x2="982" y2="54"/><line x1="980" y1="52" x2="980" y2="300"/>
  </svg>
  <div class="brand">Copperleaf Roasting House</div>
  <div class="icon-box icon-box--persona" role="img" aria-label="Glasses and moustache icon"></div>
  <p class="owner">Reid Castell</p>
  <svg class="phone-icon" viewBox="0 0 76 76" aria-hidden="true">
    <circle cx="38" cy="38" r="34" fill="none" stroke="var(--ink)" stroke-width="4"/>
    <path d="M26 20 l8 0 l3 10 l-5 4 q4 9 12 13 l4 -5 l10 3 l0 8 q-2 4 -7 4 q-16 -2 -27 -17 q-5 -8 -5 -15 q1 -5 7 -5z" fill="var(--ink)"/>
  </svg>
  <p class="phone">0491362847</p>
  <div class="contact-row">
    <svg class="pin-icon" viewBox="0 0 30 42" aria-hidden="true">
      <path d="M15 2 a13 13 0 0 1 13 13 c0 10 -13 25 -13 25 s-13 -15 -13 -25 a13 13 0 0 1 13 -13z" fill="var(--ink)"/>
      <circle cx="15" cy="15" r="5" fill="var(--kraft-light)"/>
    </svg>
    <span class="contact-row__address">61 Walden Crescent, Oakvale</span>
    <span class="social-mark" aria-hidden="true"></span>
    <span class="contact-row__handle">@copperleafroastinghouse</span>
  </div>
</section>

<section class="card card--slate">
  <svg class="card__frame" viewBox="0 0 1005 574" aria-hidden="true">
    <line x1="18" y1="52" x2="517" y2="52"/><line x1="20" y1="50" x2="20" y2="472"/>
    <line x1="705" y1="52" x2="982" y2="52"/><line x1="980" y1="50" x2="980" y2="480"/>
  </svg>
  <div class="icon-box icon-box--beans" role="img" aria-label="Two coffee beans icon"></div>
  <div class="brand">Copperleaf Roasting House</div>
  <div class="icon-box icon-box--persona" role="img" aria-label="Glasses and moustache icon"></div>
  <p class="owner">Reid Castell</p>
  <svg class="phone-icon" viewBox="0 0 76 76" aria-hidden="true">
    <circle cx="38" cy="38" r="34" fill="none" stroke="var(--ink)" stroke-width="4"/>
    <path d="M26 20 l8 0 l3 10 l-5 4 q4 9 12 13 l4 -5 l10 3 l0 8 q-2 4 -7 4 q-16 -2 -27 -17 q-5 -8 -5 -15 q1 -5 7 -5z" fill="var(--ink)"/>
  </svg>
  <p class="phone">0491362847</p>
  <div class="contact-row">
    <svg class="pin-icon" viewBox="0 0 30 42" aria-hidden="true">
      <path d="M15 2 a13 13 0 0 1 13 13 c0 10 -13 25 -13 25 s-13 -15 -13 -25 a13 13 0 0 1 13 -13z" fill="var(--ink)"/>
      <circle cx="15" cy="15" r="5" fill="var(--slate-dark)"/>
    </svg>
    <span class="contact-row__address">23 Pellow Avenue, Brindlemoor</span>
    <span class="social-mark" aria-hidden="true"></span>
    <span class="contact-row__handle">@copperleafroastinghouse</span>
  </div>
</section>

</body>
</html>
```